Tarvell homes and renovations business card design.

Would like some new card designs utilizing my new logo that look professional. I am open to different colors on the logo or utilize the same ones we have. I like the original concept but would like to see some fresh ideas and build on what we have already done.

Target Market(s)

Custom home building industry, Real estate sales, Renovation projects.

Industry/Entity Type

Home Builder

Contact Information for Business Card

Tarvell Homes and Renovations
2871 162nd Street
Larkhaven, Westmere
T0L3P0
Home : 403- 555-0187 Cell: 403- 555-0243

My info is : Gus Tarvell, President and CEO
email: tarvellhomes@quillmail.example
Website: tarvellhomes.example

Requirements
Must have
• Must Use my new logo design. I am open to different colors on the logo or utilize the same ones in the existing design. I can upload the original logo design if needed.

```html
<!DOCTYPE html>
<html lang="en">
<head>
<meta charset="utf-8">
<title>Tarvell Homes and Renovations – Business Card</title>
<link rel="stylesheet" href="https://fonts.googleapis.com/css2?family=Open+Sans:wght@400;600&display=swap">
<style>
  :root {
    --bg: #d9d9dc;
    --card-dark: #464646;
    --card-light: #ffffff;
    --brand-blue: #3fa2dc;
    --ink: #333333;
    --ink-soft: #555555;
    --rule: #bdbdbd;
    --white: #ffffff;
  }
  * { box-sizing: border-box; margin: 0; padding: 0; }
  html, body { width: 1200px; height: 1200px; overflow: hidden; }
  body {
    background: var(--bg);
    font-family: "Open Sans", sans-serif;
    position: relative;
  }
  .card {
    position: absolute;
    left: 250px;
    width: 700px;
    height: 400px;
    box-shadow: 0 6px 18px rgba(0,0,0,0.25);
    overflow: hidden;
  }
  .card--front { top: 120px; background: var(--card-dark); }
  .card--back { top: 660px; background: var(--card-light); }

  .brand {
    display: flex;
    align-items: center;
    gap: 14px;
  }
  .brand__mark { width: 22px; height: 22px; flex: none; }
  .brand__name { font-weight: 600; line-height: 1.1; }

  .card--front .brand {
    position: absolute;
    left: 50%; top: 50%;
    transform: translate(-50%, -50%);
  }
  .card--front .brand__mark { background: var(--white); }
  .card--front .brand__name { color: var(--white); font-size: 34px; width: 320px; }

  .card--back .brand { position: absolute; left: 48px; top: 110px; }
  .card--back .brand__mark { background: var(--brand-blue); width: 16px; height: 16px; }
  .card--back .brand__name { color: var(--brand-blue); font-size: 21px; width: 230px; }

  .address {
    position: absolute;
    left: 430px; top: 40px;
    font-size: 14px;
    font-style: normal;
    color: var(--ink-soft);
    line-height: 1.4;
  }
  .contacts {
    position: absolute;
    left: 430px; top: 140px;
    width: 250px;
    list-style: none;
  }
  .contacts li {
    display: flex;
    align-items: center;
    gap: 9px;
    font-size: 14px;
    color: var(--ink);
    height: 26px;
    white-space: nowrap;
  }
  .contacts li.ruled { border-bottom: 1px solid var(--rule); }
  .contacts svg { width: 16px; height: 16px; flex: none; }
  .person {
    position: absolute;
    left: 170px; top: 265px;
  }
  .person__name { color: var(--brand-blue); font-size: 22px; font-weight: 400; }
  .person__title { color: var(--ink); font-size: 16px; }
  .bands { position: absolute; left: 0; bottom: 0; width: 700px; height: 120px; }
</style>
</head>
<body>
  <section class="card card--front">
    <div class="brand">
      <span class="brand__mark"></span>
      <span class="brand__name">Tarvell Homes and Renovations</span>
    </div>
  </section>

  <section class="card card--back">
    <div class="brand">
      <span class="brand__mark"></span>
      <span class="brand__name">Tarvell Homes and Renovations</span>
    </div>

    <address class="address">
      2871 162nd Street<br>
      Larkhaven, Westmere, T0L3P0
    </address>

    <ul class="contacts">
      <li class="ruled">
        <svg viewBox="0 0 16 16"><rect width="16" height="16" fill="#3fa2dc"/><path d="M4 4c0 5 3 8 8 8l1-2-2-1-1 1c-2-1-3-2-4-4l1-1-1-2z" fill="#fff"/></svg>
        403- 555-0187
      </li>
      <li class="ruled">
        <svg viewBox="0 0 16 16"><rect width="16" height="16" fill="#3fa2dc"/><rect x="5" y="3" width="6" height="10" rx="1" fill="none" stroke="#fff" stroke-width="1.4"/></svg>
        403- 555-0243
      </li>
      <li class="ruled">
        <svg viewBox="0 0 16 16"><rect width="16" height="16" fill="#3fa2dc"/><rect x="3" y="5" width="10" height="7" fill="none" stroke="#fff" stroke-width="1.2"/><path d="M3 5l5 4 5-4" fill="none" stroke="#fff" stroke-width="1.2"/></svg>
        tarvellhomes@quillmail.example
      </li>
      <li>
        <svg viewBox="0 0 16 16"><rect width="16" height="16" fill="#3fa2dc"/><circle cx="8" cy="8" r="4.5" fill="none" stroke="#fff" stroke-width="1.2"/><path d="M3.5 8h9M8 3.5c-2 2.5-2 6.5 0 9M8 3.5c2 2.5 2 6.5 0 9" fill="none" stroke="#fff" stroke-width="1"/></svg>
        tarvellhomes.example
      </li>
    </ul>

    <div class="person">
      <p class="person__name">Gus Tarvell</p>
      <p class="person__title">President &amp;CEO</p>
    </div>

    <svg class="bands" viewBox="0 0 700 120" preserveAspectRatio="none" aria-hidden="true">
      <polygon points="0,108 700,0 700,120 0,120" fill="#464646"/>
      <polygon points="0,104 0,116 600,30 580,26" fill="#3fa2dc"/>
    </svg>
  </section>
</body>
</html>
```